Grins of Maplecrest - Dental, needs a redesign

Purpose:
Redesign website: http://www.grinsofmaplecrest.example/

Sections are important, but for content, we can use existing website or have some placeholder text to fill in later.

Some of the required sections:
About us, contact us, services, our offices, our staff, patient education, patient forms (link to Molvaro can be used here), link to friendwall, testimonials

Editability:
We would like to be able to update and edit the content in the future, for small changes

Pictures:
Here is a link to the staff pictures we’d like to use on the website:
https://www.filecrate.example/sh/503k7pq2vv884x9/BBDPyrTe_wKQj7ZumfXKTgghb?dl=0
You don't have to use all the pictures; just a few.

Friendwall page:
https://www.friendwall.example/Grins-of-Maplecrest-527163048915276

Colors: Calming colors/images for a soothing feeling... to assure the patient that it'll not be that bad.

Target Market(s)

General population

Industry/Entity Type

Dental Clinic

Coding

Coded - Design and coding required

Number of Pages Required

5+ page

Requirements
Must have
• About us, contact us, services, our offices, our staff, patient education, patient forms (link to Molvaro can be used here), link to friendwall, testimonials.
• Just create the placeholders for content or use from existing website.
• The staff picture of everyone needs to be on the home page - because that makes it more personal and has received positive feedback from many patients.

```html
<!DOCTYPE html>
<html lang="en">
<head>
<meta charset="utf-8">
<title>Grins of Maplecrest - Dental</title>
<link rel="stylesheet" href="https://fonts.googleapis.com/css2?family=Montserrat:wght@500;600;700&family=Open+Sans:ital,wght@0,400;0,600;0,700;1,400&display=swap">
<style>
:root{
  --teal:#4ccfd8;
  --teal-dark:#33bfc9;
  --purple:#a98bf0;
  --ink:#1f1f1f;
  --text:#444;
  --muted:#777;
  --line:#d6d6d6;
  --panel:#f1f1f1;
  --soft:#f7f7f7;
  --footer:#050505;
  --white:#fff;
}
*{margin:0;padding:0;box-sizing:border-box}
html,body{width:1200px;height:2514px;overflow:hidden;background:var(--white)}
body{position:relative;font-family:"Open Sans",Arial,sans-serif;color:var(--text)}
.abs{position:absolute;white-space:nowrap}
.wrap{white-space:normal}

/* header */
.appt-btn{left:608px;top:22px;width:258px;height:37px;background:var(--purple);color:#fff;border-radius:3px;font:700 15px "Open Sans",sans-serif;letter-spacing:.4px;display:flex;align-items:center;gap:12px;padding-left:12px}
.call{left:888px;top:20px;display:flex;align-items:center;gap:12px;color:var(--ink)}
.call-label{font:700 13px "Open Sans",sans-serif;letter-spacing:1px;line-height:1.2}
.call-number{font:400 21px "Open Sans",sans-serif;line-height:1.2}
.navbar{left:0;top:84px;width:1200px;height:47px;background:var(--teal)}
.brand-tab{left:117px;top:78px;width:210px;height:42px;background:#fff;border-radius:0 0 22px 22px;display:flex;align-items:center;justify-content:center}
.brand-name{font:600 15.5px "Montserrat",sans-serif;color:var(--teal);letter-spacing:.2px}
.nav{left:340px;top:84px;height:47px;display:flex;align-items:center}
.nav a{color:#fff;text-decoration:none;font:700 14.5px "Open Sans",sans-serif;padding:0 13px;border-right:1px solid rgba(255,255,255,.7);line-height:16px}
.nav a:last-child{border-right:0}

/* hero */
.hero{left:0;top:131px;width:1200px;height:452px;background:linear-gradient(90deg,#f4f6f3 0%,#eef3e6 30%,#dfe9cf 50%,#e8e2da 72%,#eed6cf 86%,#f2ece8 100%)}
.hero-text{left:97px;top:338px;width:560px;text-align:center;font:600 26px/1.33 "Montserrat",sans-serif;color:var(--ink)}
.hero-dots{left:340px;top:488px;display:flex;gap:5px}
.hero-dots i{width:9px;height:9px;border-radius:50%;background:#222;display:block}

/* services */
.services{left:0;top:583px;width:1200px;height:369px;background:var(--soft)}
.service{top:645px;width:240px;text-align:center}
.service-icon{width:104px;height:104px;margin:0 auto;border:2.5px solid var(--teal);border-radius:50%;background:#fff;display:flex;align-items:center;justify-content:center}
.service-title{margin-top:22px;font:600 16.5px/1.25 "Montserrat",sans-serif;color:var(--ink)}
.service-text{margin-top:13px;font:400 13px/1.45 "Open Sans",sans-serif;color:var(--text)}
.read-more{font:700 11px "Open Sans",sans-serif;color:var(--teal);letter-spacing:.3px}
.service .read-more{display:block;margin-top:10px}
.vdivider{width:1px;background:var(--line)}

/* welcome */
.welcome{left:0;top:952px;width:1200px;height:355px;background:var(--panel)}
.section-title{font:600 23px "Montserrat",sans-serif;letter-spacing:.3px}
.section-title .a{color:var(--purple)}
.section-title .b{color:var(--teal)}
.rule{height:1px;background:var(--line)}
.welcome-copy{left:131px;top:1071px;width:515px;font:400 13.2px/25px "Open Sans",sans-serif;color:var(--ink)}
.video{left:694px;top:1011px;width:374px;height:249px;background:linear-gradient(160deg,#d4cfc4 0%,#8d8678 45%,#4a4740 100%)}
.video-play{left:862px;top:1113px;width:56px;height:38px;background:#111;border-radius:8px;display:flex;align-items:center;justify-content:center}
.video-bar{left:694px;top:1225px;width:374px;height:35px;background:linear-gradient(#3a3a3a,#151515);display:flex;align-items:center;gap:12px;padding-left:12px}
.video-track{width:200px;height:6px;background:#555;border-radius:3px;margin-left:10px;position:relative}
.video-track span{position:absolute;left:0;top:0;height:6px;width:95px;background:#3f8fe0;border-radius:3px}

/* team */
.team-title{left:0;top:1364px;width:1200px;text-align:center}
.member{top:1488px;width:170px;text-align:center}
.member-ring{width:131px;height:131px;margin:0 auto;border:2px solid var(--teal);border-radius:50%;padding:5px;background:#fff}
.member-photo{width:100%;height:100%;border-radius:50%;background:radial-gradient(circle at 50% 40%,#c9a58c 0%,#8a6c57 55%,#4d3e35 100%)}
.member-name{margin-top:12px;font:700 14px "Montserrat",sans-serif;color:var(--ink)}

/* booking + testimonials */
.lower{left:0;top:1693px;width:1200px;height:410px;background:var(--panel)}
.field{background:#fff;border:1px solid #dcdcdc;font:400 11px "Open Sans",sans-serif;color:#333;padding:9px 10px}
.submit{left:486px;top:2016px;width:82px;height:27px;background:var(--teal);color:#fff;font:700 12px "Open Sans",sans-serif;letter-spacing:.8px;display:flex;align-items:center;justify-content:center}
.quote-box{left:630px;top:1835px;width:436px;height:152px;background:#fff;border-radius:10px;padding:13px 16px 0 56px;font:italic 400 12.4px/24px "Open Sans",sans-serif;color:var(--ink);overflow:hidden}
.quote-mark{left:650px;top:1838px;font:700 46px Georgia,serif;color:#c9c9c9}
.client-photo{left:655px;top:1973px;width:74px;height:74px;border-radius:50%;border:3px solid #fff;background:radial-gradient(circle at 50% 40%,#b58f79,#5a4236)}
.client-name{left:773px;top:2010px;font:700 14px "Montserrat",sans-serif;color:var(--ink)}

/* newsletter */
.newsletter{left:0;top:2103px;width:1200px;height:79px;background:var(--teal)}
.news-label{left:193px;top:2131px;font:600 19px "Montserrat",sans-serif;color:var(--ink)}
.news-input{left:469px;top:2130px;width:402px;height:39px;background:#fff;font:400 13px "Open Sans",sans-serif;color:#333;padding:11px 16px}
.news-btn{left:897px;top:2130px;width:171px;height:39px;border:2px solid #fff;color:#fff;font:700 16px "Montserrat",sans-serif;letter-spacing:2px;display:flex;align-items:center;justify-content:center}

/* footer */
.footer{left:0;top:2182px;width:1200px;height:292px;background:var(--footer)}
.foot-title{top:2204px;font:700 15px "Open Sans",sans-serif;color:#fff}
.foot-title span{color:var(--teal)}
.foot-rule{top:2234px;height:1px;background:#444}
.foot-text{font:400 12.5px/20px "Open Sans",sans-serif;color:#eee}
.quick-links{left:131px;top:2252px;list-style:none}
.quick-links li{font:400 12.5px/26px "Open Sans",sans-serif;color:#eee}
.quick-links li::before{content:"\203A";color:#999;margin-right:9px}
.contact-line{display:flex;align-items:center;gap:10px}
.map{left:563px;top:2256px;width:248px;height:168px;background:linear-gradient(135deg,#e4e2dc,#d2d0c8);border:3px solid #fff}
.hours{left:865px;top:2252px;font:400 12.5px/31px "Open Sans",sans-serif;color:#eee}
.hours td:first-child{width:80px}
.hours td:nth-child(2){width:20px}
.bottom-bar{left:0;top:2474px;width:1200px;height:40px;background:var(--teal);display:flex;align-items:center;justify-content:space-between;padding:0 131px;color:#fff;font:600 11.5px "Open Sans",sans-serif}
.follow{display:flex;align-items:center;gap:12px}
.social-square{width:24px;height:24px;background:#fff;border-radius:2px;display:block}
</style>
</head>
<body>

<!-- header -->
<div class="abs appt-btn">
  <svg width="22" height="22" viewBox="0 0 22 22" fill="none" stroke="#fff" stroke-width="2"><rect x="2" y="4" width="18" height="16" rx="2"/><line x1="2" y1="9" x2="20" y2="9"/><line x1="7" y1="1" x2="7" y2="6"/><line x1="15" y1="1" x2="15" y2="6"/></svg>
  <span>MAKE AN APPOINTMENT</span>
</div>
<div class="abs call">
  <svg width="36" height="36" viewBox="0 0 36 36"><circle cx="18" cy="18" r="16" fill="none" stroke="#1f1f1f" stroke-width="2.5"/><path d="M12 10c1-1 2-1 3 0l2 3c.5 1 0 2-1 2.5-.5.5 0 2 2 4s3.5 2.5 4 2c.5-1 1.5-1.5 2.5-1l3 2c1 1 1 2 0 3-2 2-5 2-9-2s-8-8-6.5-13.5z" fill="#1f1f1f"/></svg>
  <div><div class="call-label">CALL US TODAY</div><div class="call-number">(555) 013-4820</div></div>
</div>
<div class="abs navbar"></div>
<div class="abs brand-tab"><span class="brand-name">GRINS OF MAPLECREST</span></div>
<nav class="abs nav">
  <a>HOME</a><a>ABOUT US</a><a>SERVICES</a><a>OUR STAFF</a><a>TESTIMONIALS</a><a>OUR OFFICES</a><a>CONTACT US</a>
</nav>

<!-- hero -->
<div class="abs hero" role="img" aria-label="Photo of a smiling patient with a dental mirror against a soft green background"></div>
<p class="abs wrap hero-text">We are dedicated to taking the time needed to provide the very best care every patient deserves</p>
<div class="abs hero-dots"><i></i><i></i><i></i></div>

<!-- services -->
<div class="abs services"></div>
<div class="abs vdivider" style="left:355px;top:662px;height:243px"></div>
<div class="abs vdivider" style="left:605px;top:662px;height:243px"></div>
<div class="abs vdivider" style="left:855px;top:662px;height:243px"></div>

<div class="abs service" style="left:113px">
  <div class="service-icon"><svg width="46" height="56" viewBox="0 0 46 56"><path d="M23 8c-5-6-21-6-21 10 0 10 4 14 6 24 1 7 3 12 6 12s4-10 5-14c1-3 3-3 4 0 1 4 2 14 5 14s5-5 6-12c2-10 6-14 6-24C44 2 28 2 23 8z" fill="var(--teal)"/></svg></div>
  <div class="service-title">General Dental<br>Health</div>
  <div class="service-text">Lorem ipsum dolor sit amet,<br>consectetuer adipiscing<br>elit, sed</div>
  <span class="read-more">READ MORE »</span>
</div>
<div class="abs service" style="left:364px">
  <div class="service-icon"><svg width="56" height="56" viewBox="0 0 56 56"><path d="M22 10c-5-6-20-6-20 10 0 10 4 14 6 23 1 6 3 11 5 11s4-9 5-13c1-3 3-3 4 0 1 4 2 13 5 13s4-5 5-11c2-9 6-13 6-23C38 4 27 4 22 10z" fill="var(--teal)"/><path d="M46 4l2 6 6 2-6 2-2 6-2-6-6-2 6-2z" fill="var(--teal)"/></svg></div>
  <div class="service-title">Cosmetic<br>Dentistry</div>
  <div class="service-text">Lorem ipsum dolor sit amet,<br>consectetuer adipiscing<br>elit, sed</div>
  <span class="read-more">READ MORE »</span>
</div>
<div class="abs service" style="left:614px">
  <div class="service-icon"><svg width="52" height="52" viewBox="0 0 52 52"><path d="M14 26c0-14 10-20 12-10 2-10 12-4 12 10l-2 10H16z" fill="var(--teal)"/><rect x="4" y="34" width="44" height="14" rx="3" fill="var(--teal)"/></svg></div>
  <div class="service-title">Dental<br>FAQs</div>
  <div class="service-text">Lorem ipsum dolor sit amet,<br>consectetuer adipiscing<br>elit, sed</div>
  <span class="read-more">READ MORE »</span>
</div>
<div class="abs service" style="left:862px">
  <div class="service-icon"><svg width="56" height="56" viewBox="0 0 56 56"><path d="M24 8c-5-6-21-6-21 10 0 10 4 14 6 24 1 7 3 12 6 12s4-10 5-14c1-3 3-3 4 0 1 4 2 14 5 14s5-5 6-12c2-10 6-14 6-24C42 2 29 2 24 8z" fill="var(--teal)"/><circle cx="30" cy="26" r="9" fill="#fff" stroke="#fff" stroke-width="2"/><circle cx="30" cy="26" r="6" fill="none" stroke="var(--teal)" stroke-width="3"/><line x1="35" y1="31" x2="46" y2="44" stroke="var(--teal)" stroke-width="4" stroke-linecap="round"/></svg></div>
  <div class="service-title">Advanced Dental<br>Procedures</div>
  <div class="service-text">Lorem ipsum dolor sit amet,<br>consectetuer adipiscing<br>elit, sed</div>
  <span class="read-more">READ MORE »</span>
</div>

<!-- welcome -->
<div class="abs welcome"></div>
<svg class="abs" style="left:131px;top:1004px" width="32" height="32" viewBox="0 0 32 32"><circle cx="16" cy="16" r="13" fill="none" stroke="var(--purple)" stroke-width="2.5"/></svg>
<h2 class="abs section-title" style="left:176px;top:1006px"><span class="a">WELCOME TO </span><span class="b">GRINS OF MAPLECREST</span></h2>
<div class="abs rule" style="left:131px;top:1043px;width:506px"></div>
<p class="abs wrap welcome-copy">Dr. Meera Anand provides a full range of dental services to the whole family. Many of our patient families span multiple generations. Our Team are dedicated to taking the time needed to provide the very best care every patient deserves. Please tour our web site to learn more about family dentistry, cosmetic dentistry and our restorative dental services. We invite you to call us with any questions you may have - we all look forward to meeting you and your family!</p>
<span class="abs read-more" style="left:131px;top:1242px">READ MORE »</span>
<div class="abs vdivider" style="left:667px;top:1011px;height:249px"></div>
<div class="abs video" role="img" aria-label="Video still of a staff member in the treatment room"></div>
<div class="abs video-play"><svg width="18" height="20" viewBox="0 0 18 20"><path d="M2 1l15 9-15 9z" fill="#fff"/></svg></div>
<div class="abs video-bar">
  <svg width="12" height="14" viewBox="0 0 12 14"><path d="M1 1l10 6-10 6z" fill="#fff"/></svg>
  <svg width="16" height="14" viewBox="0 0 16 14"><path d="M1 5h3l4-4v12l-4-4H1z" fill="#fff"/><path d="M11 4q3 3 0 6" stroke="#fff" fill="none" stroke-width="1.5"/></svg>
  <div class="video-track"><span></span></div>
</div>

<!-- team -->
<h2 class="abs section-title team-title"><span class="a">MEET </span><span class="b">OUR TEAM</span></h2>
<div class="abs rule" style="left:469px;top:1428px;width:262px"></div>
<svg class="abs" style="left:588px;top:1416px" width="24" height="24" viewBox="0 0 24 24"><circle cx="12" cy="12" r="10" fill="#fff" stroke="var(--purple)" stroke-width="2"/></svg>

<div class="abs member" style="left:118px"><div class="member-ring"><div class="member-photo" role="img" aria-label="Team member portrait"></div></div><div class="member-name">lorem ipsum</div></div>
<div class="abs member" style="left:314px"><div class="member-ring"><div class="member-photo" role="img" aria-label="Team member portrait"></div></div><div class="member-name">lorem ipsum</div></div>
<div class="abs member" style="left:508px"><div class="member-ring"><div class="member-photo" role="img" aria-label="Team member portrait"></div></div><div class="member-name">lorem ipsum</div></div>
<div class="abs member" style="left:708px"><div class="member-ring"><div class="member-photo" role="img" aria-label="Portrait of Dr. Meera Anand"></div></div><div class="member-name">Dr. Meera Anand</div></div>
<div class="abs member" style="left:904px"><div class="member-ring"><div class="member-photo" role="img" aria-label="Team member portrait"></div></div><div class="member-name">lorem ipsum</div></div>

<!-- booking + testimonials -->
<div class="abs lower"></div>
<svg class="abs" style="left:131px;top:1756px" width="22" height="18" viewBox="0 0 22 18"><rect x="1" y="2" width="20" height="14" rx="1" fill="var(--purple)"/><path d="M1 3l10 7 10-7" stroke="#fff" stroke-width="1.8" fill="none"/></svg>
<h2 class="abs section-title" style="left:168px;top:1751px"><span class="a">BOOK AN </span><span class="b">APPOINTMENT</span></h2>
<div class="abs rule" style="left:131px;top:1795px;width:435px"></div>
<div class="abs field" style="left:131px;top:1835px;width:206px;height:34px">Patient Name</div>
<div class="abs field" style="left:359px;top:1835px;width:207px;height:34px">Appointment Date</div>
<div class="abs field" style="left:131px;top:1885px;width:206px;height:34px">Gender</div>
<div class="abs field" style="left:359px;top:1885px;width:207px;height:34px">Contact No</div>
<div class="abs field" style="left:131px;top:1934px;width:435px;height:66px">Message</div>
<div class="abs submit">SUBMIT</div>

<svg class="abs" style="left:625px;top:1756px" width="24" height="20" viewBox="0 0 24 20"><rect x="0" y="0" width="15" height="11" rx="2" fill="var(--purple)"/><rect x="8" y="5" width="15" height="11" rx="2" fill="var(--purple)" stroke="var(--panel)" stroke-width="1.5"/><path d="M18 16v4l-4-4z" fill="var(--purple)"/></svg>
<h2 class="abs section-title" style="left:660px;top:1751px"><span class="a">CLIENT </span><span class="b">TESTIMONIALS</span></h2>
<svg class="abs" style="left:1041px;top:1762px" width="24" height="14" viewBox="0 0 24 14" fill="none" stroke="#555" stroke-width="2"><path d="M7 2l-5 5 5 5M17 2l5 5-5 5"/></svg>
<div class="abs rule" style="left:625px;top:1795px;width:441px"></div>
<div class="abs wrap quote-box">Lorem ipsum dolor sit amet consetug e sed diay nibh euismodl tincidunt ut laoreet dolore magam er vol wisi enim ad minim veniam quis nostrud exerci tationorem ipsum dolor sit ametee sed diammmy nibh euismd tincidunt ut laoreet dolore magna aliqur volpatl tiidunt ut laoreet dolore magna</div>
<svg class="abs" style="left:938px;top:1986px" width="66" height="26" viewBox="0 0 66 26"><path d="M0 0h66L0 26z" fill="#fff"/></svg>
<div class="abs quote-mark">“</div>
<div class="abs client-photo" role="img" aria-label="Client portrait"></div>
<div class="abs client-name">Mr. Calvin Rowe</div>

<!-- newsletter -->
<div class="abs newsletter"></div>
<svg class="abs" style="left:133px;top:2120px" width="46" height="46" viewBox="0 0 46 46"><circle cx="23" cy="23" r="21" fill="none" stroke="#fff" stroke-width="2.5"/><rect x="12" y="15" width="22" height="16" rx="1" fill="#fff"/><path d="M12 16l11 8 11-8" stroke="var(--teal)" stroke-width="1.8" fill="none"/></svg>
<div class="abs news-label">Sign Up For Newsletter</div>
<div class="abs news-input">Enter your email here</div>
<div class="abs news-btn">SUBSCRIBE</div>

<!-- footer -->
<div class="abs footer"></div>
<div class="abs foot-title" style="left:131px">Quick <span>Links</span></div>
<div class="abs foot-title" style="left:297px">Contact <span>Details</span></div>
<div class="abs foot-title" style="left:563px">Location <span>Map</span></div>
<div class="abs foot-title" style="left:865px">Opening <span>Hours</span></div>
<div class="abs foot-rule" style="left:131px;width:113px"></div>
<div class="abs foot-rule" style="left:297px;width:213px"></div>
<div class="abs foot-rule" style="left:563px;width:248px"></div>
<div class="abs foot-rule" style="left:865px;width:205px"></div>

<ul class="abs quick-links">
  <li>Home</li><li>About Us</li><li>Services</li><li>Our Staff</li><li>Testimonials</li><li>Our Offices</li><li>Contact Us</li>
</ul>

<div class="abs foot-text" style="left:297px;top:2253px">GRINS OF MAPLECREST<br>4810 W. Linden Ave, Suite 2C<br>Maplecrest, IL 60000</div>
<div class="abs foot-text contact-line" style="left:297px;top:2333px"><svg width="12" height="12" viewBox="0 0 12 12"><path d="M2 1c1-1 2 0 2.5 1l.5 1.5c0 .7-.5 1-1 1.3.6 1.4 1.6 2.4 3 3 .3-.5.6-1 1.3-1l1.5.5c1 .5 2 1.5 1 2.5C9 12 0 3 2 1z" fill="var(--teal)"/></svg><span style="margin-left:10px">555-014-2290</span></div>
<div class="abs foot-text contact-line" style="left:297px;top:2368px"><svg width="12" height="12" viewBox="0 0 12 12"><path d="M2 1c1-1 2 0 2.5 1l.5 1.5c0 .7-.5 1-1 1.3.6 1.4 1.6 2.4 3 3 .3-.5.6-1 1.3-1l1.5.5c1 .5 2 1.5 1 2.5C9 12 0 3 2 1z" fill="var(--teal)"/></svg><span style="margin-left:10px">555-014-2291</span></div>
<div class="abs foot-text contact-line" style="left:297px;top:2407px"><svg width="14" height="10" viewBox="0 0 14 10"><rect width="14" height="10" fill="var(--teal)"/><path d="M0 1l7 5 7-5" stroke="#000" stroke-width="1.2" fill="none"/></svg><span>info@grinsofmaplecrest.example</span></div>

<div class="abs map" role="img" aria-label="Street map showing the clinic location"></div>
<svg class="abs" style="left:662px;top:2306px" width="24" height="34" viewBox="0 0 24 34"><path d="M12 0C5 0 0 5 0 12c0 9 12 22 12 22s12-13 12-22C24 5 19 0 12 0z" fill="#e04a3c"/><circle cx="12" cy="12" r="4.5" fill="#fff"/></svg>

<table class="abs hours">
  <tr><td>Monday</td><td>-</td><td>12:00pm to 6:00pm</td></tr>
  <tr><td>Tuesday</td><td>-</td><td>10:00am to 7:00pm</td></tr>
  <tr><td>Wednesday</td><td>-</td><td>Closed</td></tr>
  <tr><td>Thursday</td><td>-</td><td>8:00am to 6:00pm</td></tr>
  <tr><td>Friday</td><td>-</td><td>8:00am to 5:00pm</td></tr>
  <tr><td>Saturday</td><td>-</td><td>8:00am to 12:00pm</td></tr>
</table>

<div class="abs bottom-bar">
  <span>Copyright 2016 GRINS OF MAPLECREST &nbsp;|&nbsp; All Rights Reserved</span>
  <span class="follow">Follow Us On : <i class="social-square"></i></span>
</div>

</body>
</html>
```